Verpackungsdesign für Wellness- und Saunaprodukte
Zielgruppe
Brisavo ist ein junges Start-Up, das sich auf Wellness- und Saunaprodukte spezialisiert hat. Unsere Zielgruppe besteht zu beinahe gleichen Teilen aus männlichen und weiblichen Personen zwischen 30 und 60 Jahren. Unsere Produkte befinden sich eher im mittel- bis höherpreisigen Segment, daher streben wir ein hochwertiges Design für unsere Verpackungen an. Unsere Produktpalette reicht von Mentholkristallen, Saunaaufgüssen, bis hin zu Textilien für den Wellnessbereich und soll dementsprechend Menschen ansprechen, die sich einen gewissen Luxus im Alltag auch gönnen.
Aufgabenstellung
Inspiriert von der skandinavischen Sauna Kultur, möchten wir Momente der Erholung und
Entspannung in den Alltag unserer Kunden bringen. Die Geschichte des Saunierens ist eng mit der skandinavischen Kultur verbunden und skandinavische Stilelemente sind zeitgemäß und sprechen ein breites Publikum an. Das Design muss auf Dosen/Tiegel , Karton Verpackungen und Flaschen verschiedener Größen adaptierbar sein (siehe Bild im Anhang).
40g Tiegel(transparent) Höhe 40mm Durchmesser 60mm (ohne Deckel Silber gebürstet)
100g Tiegel(transparent) Höhe 53mm Durchmesser 71mm (ohne Deckel Silber gebürstet)
200g Tiegel(transparent) Höhe 65mm Durchmesser 90mm (ohne Deckel Silber gebürstet)
Karton Verpackung 124,5x49x49mm
Karton Verpackung 100x100x100mm
Flaschenetikett 134x67mm (Braunglas, schwarzer Deckel)
Es soll ein passendes Keyvisual erstellt werden.
Im Anhang sieht man die Verpackungen, Dosen, Flaschen sowie unsere ersten Design Entwürfe (an diese Anordnung der Elemente kann sich der Designer orientieren ). Das Logo bleibt wie gegeben. Das Produkt für die Tiegel soll Mentholkristalle sein.

```html
<!DOCTYPE html>
<html lang="de">
<head>
<meta charset="utf-8">
<title>Brisavo – Saunaaufgüsse Etiketten</title>
<link rel="stylesheet" href="https://fonts.googleapis.com/css2?family=Ubuntu:wght@400;500;700&display=swap">
<style>
  :root {
    --page-bg: #ffffff;
    --label-brown: #4a2620;
    --label-brown-deep: #3a1d18;
    --label-ink: #f6efe9;
    --label-ink-soft: #d9c6bc;
    --ornament-light: #efe3dc;
    --ornament-dark: #b99a8e;
  }
  * { margin: 0; padding: 0; box-sizing: border-box; }
  html, body {
    width: 1200px;
    height: 848px;
    overflow: hidden;
    background: var(--page-bg);
  }
  .canvas {
    position: relative;
    width: 1200px;
    height: 848px;
    font-family: "Ubuntu", sans-serif;
  }
  .label {
    position: absolute;
    top: 300px;
    width: 150px;
    height: 300px;
    background: linear-gradient(180deg, var(--label-brown) 0%, var(--label-brown-deep) 100%);
    color: var(--label-ink);
  }
  .label--granatapfel { left: 290px; }
  .label--fichte { left: 513px; }
  .label--menthol { left: 732px; }

  .label__ornament {
    position: absolute;
    top: 96px;
    left: 49px;
    width: 52px;
    height: 52px;
    border-radius: 50%;
    background: radial-gradient(circle, var(--ornament-light) 0%, var(--ornament-dark) 100%);
    opacity: 0.85;
  }
  .label__name {
    position: absolute;
    top: 184px;
    left: 16px;
    font-weight: 700;
    font-size: 16px;
    line-height: 18px;
    letter-spacing: 0.3px;
    text-transform: uppercase;
  }
  .label__tagline {
    position: absolute;
    top: 224px;
    left: 16px;
    font-size: 6.6px;
    letter-spacing: 0.4px;
    text-transform: uppercase;
    color: var(--label-ink-soft);
  }
  .label__footer {
    position: absolute;
    left: 16px;
    right: 14px;
    bottom: 16px;
    display: flex;
    justify-content: space-between;
    align-items: flex-end;
  }
  .label__usage {
    font-size: 5.6px;
    line-height: 7px;
    letter-spacing: 0.3px;
    text-transform: uppercase;
    color: var(--label-ink-soft);
  }
  .label__brand {
    font-size: 6.5px;
    font-weight: 400;
    color: var(--label-ink-soft);
  }
</style>
</head>
<body>
<main class="canvas">
  <section class="label label--granatapfel">
    <div class="label__ornament" role="img" aria-label="Sonnenspiral-Ornament"></div>
    <h2 class="label__name">Granat<br>Apfel</h2>
    <p class="label__tagline">Auszeit in der Flasche</p>
    <div class="label__footer">
      <p class="label__usage">Aufguss<br>für die Sauna</p>
      <span class="label__brand">Brisavo</span>
    </div>
  </section>

  <section class="label label--fichte">
    <div class="label__ornament" role="img" aria-label="Sonnenspiral-Ornament"></div>
    <h2 class="label__name">Nordische<br>Fichte</h2>
    <p class="label__tagline">Auszeit in der Flasche</p>
    <div class="label__footer">
      <p class="label__usage">Aufguss<br>für die Sauna</p>
      <span class="label__brand">Brisavo</span>
    </div>
  </section>

  <section class="label label--menthol">
    <div class="label__ornament" role="img" aria-label="Sonnenspiral-Ornament"></div>
    <h2 class="label__name">Menthol<br>Kristalle</h2>
    <p class="label__tagline">Auszeit in der Flasche</p>
    <div class="label__footer">
      <p class="label__usage">Aufguss<br>für die Sauna</p>
      <span class="label__brand">Brisavo</span>
    </div>
  </section>
</main>
</body>
</html>
```